Brimvane.com fiber optic internet website redesign

We need a new website design for our fiber optic internet company that provides internet, phone, and tv services. It should use the text "Marrowfen fiber optics", and "I beamed up with Marrowfen". The design should use the color blue and the attached logo.
We are a 30 year old internet company who started as a dial up internet provider in our basement. Today we design, build, and maintain our own fiber optic internet network to provide service to residential, business, educational, healthcare, and governmental customers

```html
<!DOCTYPE html>
<html lang="en">
<head>
<meta charset="utf-8">
<title>Brimvane.com — Marrowfen Fiber Optics</title>
<link href="https://fonts.googleapis.com/css2?family=Manrope:wght@400;500;600;700&family=Plus+Jakarta+Sans:wght@400;500;600;700&display=swap" rel="stylesheet">
<style>
:root{
  --navy:#001355;
  --blue:#094fb1;
  --sky:#bdcfef;
  --mist:#d2e0fa;
  --grey:#d3d3d3;
  --paper:#f1f1f1;
  --ink:#14182b;
  --muted:#6b7280;
  --board:#b4b7c2;
  --card:#f5f7fc;
}
*{margin:0;padding:0;box-sizing:border-box}
html,body{width:1200px;height:3994px;overflow:hidden}
body{background:var(--board);font-family:"Plus Jakarta Sans",sans-serif;color:var(--ink);position:relative}
.abs{position:absolute}
.brand-sheet .wordmark{left:183px;top:104px;display:flex;align-items:center;gap:10px}
.dot{width:38px;height:38px;border-radius:50%;background:var(--blue)}
.wordmark .name{font-family:"Manrope",sans-serif;font-weight:700;font-size:17px;letter-spacing:1.5px;color:var(--blue)}
.wordmark .tag{font-size:8px;letter-spacing:1px;color:var(--blue);margin-top:2px;text-transform:uppercase}
.sheet-title{font-family:"Manrope",sans-serif;font-size:26px;color:var(--navy);font-weight:500}
.font-list{font-family:"Manrope",sans-serif;font-size:15px;color:#5b6275;line-height:23px;margin-top:8px}
.swatches{display:flex;gap:8px;margin-top:10px}
.swatch{width:42px;text-align:center;font-size:7px;color:#2c3350}
.swatch i{display:block;width:42px;height:42px;border-radius:50%;margin-bottom:7px}

.site{position:absolute;left:202px;top:271px;width:795px;height:3617px;background:#fff;overflow:hidden}
.hero{left:0;top:0;width:795px;height:460px;background:linear-gradient(180deg,#0a1a66 0%,#071551 50%,#04103f 100%)}
.globe{left:-40px;top:200px;width:875px;height:300px;border-radius:50% 50% 0 0/60% 60% 0 0;background:radial-gradient(ellipse at 50% 70%,#2f8cf0 0%,#1457c4 35%,#0a2b86 65%,rgba(4,16,63,0) 85%)}
.nav{left:0;top:0;width:795px;height:40px;font-size:8px;color:#fff}
.nav .wordmark{left:51px;top:10px;display:flex;align-items:center;gap:6px}
.nav .dot{width:20px;height:20px;background:#2f6fd4}
.nav .name{font-family:"Manrope",sans-serif;font-weight:700;font-size:10px;letter-spacing:1px;color:#fff}
.nav .tag{font-size:5px;letter-spacing:.6px;color:#fff;text-transform:uppercase}
.menu span{position:absolute;top:18px}
.support-btn{left:681px;top:10px;width:62px;height:22px;background:#fff;color:var(--blue);border-radius:3px;font-weight:600;display:flex;align-items:center;justify-content:center;gap:3px}
.hero-title{left:0;top:80px;width:795px;text-align:center;font-family:"Manrope",sans-serif;font-weight:700;font-size:42px;color:#fff}
.hero-title em{font-style:normal;color:#3b8cf0}
.hero-sub{left:0;top:137px;width:795px;text-align:center;font-size:9px;color:#d8e0f5}
.search{left:239px;top:177px;width:319px;height:37px;border:1px solid rgba(255,255,255,.35);border-radius:5px;background:rgba(0,19,85,.6);font-size:7.5px;color:#b8c3e0}
.search .ph{position:absolute;left:10px;top:14px}
.search .go{position:absolute;right:5px;top:6px;height:25px;width:82px;background:var(--blue);color:#fff;border-radius:4px;font-size:7px;font-weight:600;display:flex;align-items:center;justify-content:center}

.center{left:0;width:795px;text-align:center}
.intro h2{font-family:"Manrope",sans-serif;font-weight:500;font-size:22px;line-height:26px;color:var(--ink)}
.hl{color:var(--blue)}
.small{font-size:9px;color:var(--muted);line-height:13px}
.pills{left:0;top:650px;width:795px;display:flex;justify-content:center;gap:8px}
.pill{width:116px;height:40px;background:#eef2fa;border-radius:3px;font-size:9px;display:flex;align-items:center;justify-content:center;gap:6px;color:var(--ink)}
.sec-title{font-family:"Manrope",sans-serif;font-weight:500;font-size:27px;color:var(--ink)}

.sol{border-radius:6px;background:linear-gradient(135deg,#d9e5fb 0%,#c2d5f5 100%);overflow:hidden}
.sol h3{position:absolute;font-family:"Manrope",sans-serif;font-weight:500;font-size:14px}
.sol p{position:absolute;font-size:8.5px;line-height:13px;color:#4b5365;width:200px}
.btn-o{position:absolute;height:24px;width:80px;border:1px solid var(--blue);color:var(--blue);border-radius:3px;font-size:7px;display:flex;align-items:center;justify-content:center;gap:4px}
.btn-f{background:var(--blue);color:#fff}
.ph-img{position:absolute;background:linear-gradient(135deg,#8a93a3,#c9cfd8)}

.help-card{border-radius:6px;overflow:hidden}
.help-card .label{position:absolute;left:24px;bottom:32px;color:#fff;font-family:"Manrope",sans-serif;font-weight:600;font-size:14px}
.help-card .tags{position:absolute;left:24px;bottom:14px;color:#fff;font-size:7px;display:flex;gap:14px}

.tst{background:var(--card);border-radius:6px;width:174px;height:174px}
.tst .stars{position:absolute;left:22px;top:24px;color:var(--blue);font-size:8px;letter-spacing:1px}
.tst p{position:absolute;left:22px;top:42px;width:135px;font-size:7px;line-height:11px;color:#555c6e}
.tst .who{position:absolute;left:22px;top:120px;display:flex;gap:8px;align-items:center;font-size:7px}
.av{width:22px;height:22px;border-radius:50%;background:#c7b7a5}
.who small{display:block;color:#a0a6b4;font-size:5.5px}

.plan{width:225px;height:358px;background:var(--card);border-radius:6px;overflow:hidden}
.plan .top{position:absolute;left:0;top:0;width:225px;height:86px;background:#dfe8fa}
.plan.feat .top{background:var(--blue)}
.plan .lbl{position:absolute;left:20px;top:18px;font-size:7.5px;color:var(--blue)}
.plan .price{position:absolute;left:20px;top:34px;font-family:"Manrope",sans-serif;font-weight:700;font-size:30px;color:var(--navy)}
.plan .price small{font-size:9px;font-weight:400;color:var(--blue)}
.plan.feat .lbl,.plan.feat .price,.plan.feat .price small{color:#fff}
.plan .desc{position:absolute;left:20px;top:106px;width:180px;font-size:7.5px;line-height:11px;color:#636a7a}
.plan .rule{position:absolute;left:20px;top:148px;width:185px;border-top:1px solid #e2e5ec}
.plan ul{position:absolute;left:20px;top:168px;list-style:none;font-size:7.5px;color:#3b4150}
.plan li{height:25px;display:flex;align-items:center;gap:8px}
.plan .cta{position:absolute;left:20px;top:304px;width:185px;height:24px;border:1px solid var(--blue);border-radius:3px;color:var(--blue);font-size:7px;font-weight:600;display:flex;align-items:center;justify-content:center}
.plan.feat .cta{background:var(--blue);color:#fff}

.faq-item{position:absolute;left:375px;width:332px;font-size:7.5px;color:#2a3040;border-bottom:1px solid #e2e5ec;height:40px;display:flex;justify-content:space-between;align-items:flex-start;padding-top:2px}

.subscribe{left:40px;top:3204px;width:717px;height:129px;background:var(--blue);border-radius:3px}
.subscribe h3{position:absolute;left:0;top:38px;width:717px;text-align:center;color:#fff;font-family:"Manrope",sans-serif;font-weight:400;font-size:20px}
.subscribe h3 b{font-weight:700}
.sub-field{position:absolute;left:199px;top:73px;width:319px;height:30px;background:#fff;border-radius:4px;font-size:7px;color:#9aa1b0}
.sub-field span{position:absolute;left:10px;top:11px}
.sub-field .go{position:absolute;right:4px;top:4px;width:80px;height:22px;background:var(--blue);color:#fff;border-radius:3px;display:flex;align-items:center;justify-content:center;font-size:6.5px;left:auto}

.fcol{position:absolute;top:3387px;font-size:7px;color:#7a8090;line-height:17px}
.fcol h4{font-family:"Manrope",sans-serif;font-weight:600;font-size:10px;color:var(--blue);margin-bottom:2px}
.fcol b{color:#2a3040;font-weight:600}
</style>
</head>
<body>

<section class="brand-sheet">
  <div class="abs wordmark">
    <i class="dot"></i>
    <div><div class="name">BRIMVANE.COM</div><div class="tag">Marrowfen fiber optics</div></div>
  </div>
  <div class="abs" style="left:478px;top:94px">
    <div class="sheet-title">Fonts:</div>
    <div class="font-list">Manrope<br>Plus Jakarta Sans</div>
  </div>
  <div class="abs" style="left:733px;top:94px">
    <div class="sheet-title">Colors:</div>
    <div class="swatches">
      <div class="swatch"><i style="background:var(--navy)"></i>#001355</div>
      <div class="swatch"><i style="background:var(--blue)"></i>#094fb1</div>
      <div class="swatch"><i style="background:var(--sky)"></i>#bdcfef</div>
      <div class="swatch"><i style="background:var(--mist)"></i>#d2e0fa</div>
      <div class="swatch"><i style="background:var(--grey)"></i>#d3d3d3</div>
      <div class="swatch"><i style="background:var(--paper)"></i>#f1f1f1</div>
    </div>
  </div>
</section>

<main class="site">
  <!-- Hero -->
  <div class="abs hero"></div>
  <div class="abs globe" role="img" aria-label="Glowing fiber optic light trails wrapped around a night-time globe"></div>
  <svg class="abs" style="left:0;top:0" width="795" height="470" viewBox="0 0 795 470"><path d="M0 380 Q397 520 795 380 L795 470 L0 470 Z" fill="#fff"/></svg>

  <header class="abs nav">
    <div class="abs wordmark"><i class="dot"></i><div><div class="name">BRIMVANE.COM</div><div class="tag">Marrowfen fiber optics</div></div></div>
    <div class="menu">
      <span style="left:180px">Services ⌄</span>
      <span style="left:234px">Residential ⌄</span>
      <span style="left:303px">Business ⌄</span>
      <span style="left:357px">Telecom</span>
      <span style="left:403px">FAQs</span>
      <span style="left:632px">✆ Contact</span>
    </div>
    <div class="abs support-btn">
      <svg width="9" height="9" viewBox="0 0 24 24" fill="none" stroke="currentColor" stroke-width="2.5"><path d="M4 14v-2a8 8 0 0 1 16 0v2"/><rect x="3" y="14" width="4" height="6" rx="1"/><rect x="17" y="14" width="4" height="6" rx="1"/></svg>Support
    </div>
  </header>

  <h1 class="abs hero-title">I <em>Beamed Up</em> with Marrowfen</h1>
  <p class="abs hero-sub">Marrowfen brings the fiber optic technology used for years by government and industry to your home or business</p>
  <div class="abs search"><span class="ph">City, Address or Zip...</span><span class="go">⚲ Check Availability</span></div>

  <!-- Intro -->
  <section class="abs center intro" style="top:502px">
    <h2>For 30 years, Marrowfen Fiber Optic service offers<br><span class="hl">low cost</span>, <span class="hl">high quality</span>, and extremely <span class="hl">reliable</span><br>Phone, TV and high-speed Internet access.</h2>
    <p class="small" style="margin-top:20px">Utilizing our own fiber optic network, we can bring you internet speeds that far surpass<br>traditional DSL or Cable services.</p>
  </section>
  <div class="abs pills">
    <div class="pill"><svg width="16" height="16" viewBox="0 0 24 24" fill="none" stroke="#094fb1" stroke-width="1.6"><path d="M4 14v-2a8 8 0 0 1 16 0v2"/><rect x="3" y="14" width="4" height="6" rx="1"/><rect x="17" y="14" width="4" height="6" rx="1"/></svg>Local Support</div>
    <div class="pill"><svg width="16" height="16" viewBox="0 0 24 24" fill="none" stroke="#094fb1" stroke-width="1.6"><path d="M5 11h14l-2 9H7z"/><circle cx="12" cy="6" r="3"/></svg>Save Money</div>
    <div class="pill"><svg width="16" height="16" viewBox="0 0 24 24" fill="none" stroke="#094fb1" stroke-width="1.6"><circle cx="12" cy="12" r="9"/><circle cx="12" cy="12" r="5"/></svg>High Quality</div>
  </div>

  <!-- Solutions -->
  <h2 class="abs center sec-title" style="top:740px"><span class="hl">Solutions</span> We Provide</h2>
  <div class="abs sol" style="left:90px;top:797px;width:345px;height:248px">
    <h3 style="left:40px;top:36px">Dual Fiber Optic Solutions</h3>
    <p style="left:40px;top:66px">Lorem ipsum dolor sit amet, adipiscing elit, art sed do eiusmod tempor incididunt ut labore et dolore magna aliqua</p>
    <div class="btn-o" style="left:40px;top:130px">Discover More →</div>
    <div class="ph-img" role="img" aria-label="Fiber optic cable end with spread strands" style="left:210px;top:140px;width:135px;height:108px;background:radial-gradient(circle at 70% 40%,#9bb8e8,rgba(194,213,245,0) 70%)"></div>
  </div>
  <div class="ph-img" role="img" aria-label="Man with glasses on a phone call at his laptop" style="left:457px;top:797px;width:250px;height:248px;border-radius:6px;background:linear-gradient(135deg,#a9b3c2,#e2e6ec)"></div>
  <div class="abs sol" style="left:90px;top:1066px;width:250px;height:248px">
    <h3 style="left:30px;top:36px">VoIP Services</h3>
    <p style="left:30px;top:66px">Lorem ipsum dolor sit amet, adipiscing elit, art sed do eiusmod tempor incididunt ut labore et dolore magna aliqua</p>
    <div class="btn-o btn-f" style="left:30px;top:130px">Discover More →</div>
    <div class="ph-img" role="img" aria-label="Desk VoIP phone" style="left:100px;top:140px;width:150px;height:108px;background:linear-gradient(135deg,#5a6170,#2a2e38);border-radius:40px 0 0 0"></div>
  </div>
  <div class="abs sol" style="left:361px;top:1066px;width:346px;height:248px">
    <h3 style="left:40px;top:36px">Managed &amp; Virtual Hosting</h3>
    <p style="left:40px;top:66px">Lorem ipsum dolor sit amet, adipiscing elit, art sed do eiusmod tempor incididunt ut labore et dolore magna aliqua</p>
    <div class="btn-o" style="left:40px;top:130px">Discover More →</div>
    <div class="ph-img" role="img" aria-label="Server racks" style="left:230px;top:138px;width:116px;height:110px;background:linear-gradient(180deg,#3b3f48,#16181d)"></div>
  </div>

  <!-- How we help -->
  <h2 class="abs center sec-title" style="top:1366px">How We <span class="hl">Help</span> You?</h2>
  <p class="abs center small" style="top:1422px">We design, build, and maintain our own fiber optic internet network to provide service<br>to residential, business, educational, healthcare, and governmental customers</p>
  <div class="abs help-card" role="img" aria-label="Partial view of previous slide" style="left:0;top:1463px;width:20px;height:222px;background:#8d96a6"></div>
  <div class="abs help-card" style="left:40px;top:1463px;width:348px;height:222px;background:linear-gradient(180deg,#c9cbd0 0%,#8a8f99 100%)" role="img" aria-label="Mother and child relaxing together on a sofa">
    <div class="label">Residential</div>
    <div class="tags"><span>✓ Internet Service</span><span>✓ Phone Service</span><span>✓ Internet &amp; Phone Packages</span></div>
  </div>
  <div class="abs help-card" style="left:409px;top:1463px;width:348px;height:222px;background:linear-gradient(180deg,#a8b0bd 0%,#566072 100%)" role="img" aria-label="Office workers with headsets at computer desks">
    <div class="label">Business</div>
    <div class="tags"><span>✓ Internet Service</span><span>✓ Phone Service</span><span>✓ Internet &amp; Phone Packages</span></div>
  </div>
  <div class="abs help-card" role="img" aria-label="Partial view of next slide" style="left:778px;top:1463px;width:17px;height:222px;background:#8d96a6"></div>
  <div class="abs center" style="top:1708px;color:var(--blue);font-size:14px;letter-spacing:10px">←→</div>

  <!-- Feedback -->
  <section class="abs" style="left:90px;top:1964px;width:240px">
    <h2 class="sec-title" style="font-size:28px;line-height:28px">Our Clients<br><span class="hl">Feedback</span></h2>
    <p class="small" style="font-size:7.5px;line-height:11px;margin-top:14px">Utilizing our own fiber optic network, we<br>can bring you internet speeds that far<br>surpass traditional DSL or Cable</p>
    <div style="display:flex;align-items:center;gap:6px;margin-top:40px">
      <div style="display:flex"><i class="av" style="width:14px;height:14px"></i><i class="av" style="width:14px;height:14px;margin-left:-4px;background:#a58a74"></i><i class="av" style="width:14px;height:14px;margin-left:-4px;background:#d1bda9"></i></div>
      <div style="font-size:7px">4.8/5 <span style="color:#f5b800">★★★★★</span><br><span style="font-size:5px;color:#8a90a0">Based on 1K+ reviews</span></div>
    </div>
  </section>
  <div class="abs tst" style="left:340px;top:1860px"><div class="stars">★★★★★</div><p>Lorem ipsum dolor sit amet, do et eiusmod tempor incididunt ut labore et dolore magna aliqua. Quis ipsum suspendisse ultrices gravida.</p><div class="who"><i class="av"></i><div>Dana Holloway<small>Satisfied Client</small></div></div></div>
  <div class="abs tst" style="left:340px;top:2054px"><div class="stars">★★★★★</div><p>Lorem ipsum dolor sit amet, do et eiusmod tempor incididunt ut labore et dolore magna aliqua. Quis ipsum suspendisse ultrices gravida.</p><div class="who"><i class="av"></i><div>Dana Holloway<small>Satisfied Client</small></div></div></div>
  <div class="abs tst" style="left:533px;top:1781px"><div class="stars">★★★★★</div><p>Lorem ipsum dolor sit amet, do et eiusmod tempor incididunt ut labore et dolore magna aliqua. Quis ipsum suspendisse ultrices gravida.</p><div class="who"><i class="av"></i><div>Dana Holloway<small>Satisfied Client</small></div></div></div>
  <div class="abs tst" style="left:533px;top:1975px"><div class="stars">★★★★★</div><p>Lorem ipsum dolor sit amet, do et eiusmod tempor incididunt ut labore et dolore magna aliqua. Quis ipsum suspendisse ultrices gravida.</p><div class="who"><i class="av"></i><div>Dana Holloway<small>Satisfied Client</small></div></div></div>
  <div class="abs tst" style="left:533px;top:2168px"><div class="stars">★★★★★</div><p>Lorem ipsum dolor sit amet, do et eiusmod tempor incididunt ut labore et dolore magna aliqua. Quis ipsum suspendisse ultrices gravida.</p><div class="who"><i class="av"></i><div>Dana Holloway<small>Satisfied Client</small></div></div></div>

  <!-- Pricing -->
  <h2 class="abs center sec-title" style="top:2392px">Check Our <span class="hl">Pricing</span> Plans</h2>
  <div class="abs plan" style="left:42px;top:2460px">
    <div class="top"></div><div class="lbl">VoIP Phone Service - Starting at:</div>
    <div class="price">$25<small> / per month</small></div>
    <p class="desc">Our Standard Plan grants you viable access to exclusive features</p><div class="rule"></div>
    <ul><li>✓ Some text filler goes here</li><li>✓ Some text filler goes here</li><li>✓ Some text filler goes here</li><li>✓ Some text filler goes here</li><li>✓ Some text filler goes here</li></ul>
    <div class="cta">Get Started Now</div>
  </div>
  <div class="abs plan feat" style="left:287px;top:2460px">
    <div class="top"></div><div class="lbl">High Speed Internet Service - Starting at:</div>
    <div class="price">$55<small> / per month</small></div>
    <p class="desc">Our Standard Plan grants you viable access to exclusive features</p><div class="rule"></div>
    <ul><li>✓ Some text filler goes here</li><li>✓ Some text filler goes here</li><li>✓ Some text filler goes here</li><li>✓ Some text filler goes here</li><li>✓ Some text filler goes here</li></ul>
    <div class="cta">Get Started Now</div>
  </div>
  <div class="abs plan" style="left:532px;top:2460px">
    <div class="top"></div><div class="lbl">Phone &amp; Internet Packages - Starting at:</div>
    <div class="price">$80<small> / per month</small></div>
    <p class="desc">Our Standard Plan grants you viable access to exclusive features</p><div class="rule"></div>
    <ul><li>✓ Some text filler goes here</li><li>✓ Some text filler goes here</li><li>✓ Some text filler goes here</li><li>✓ Some text filler goes here</li><li>✓ Some text filler goes here</li></ul>
    <div class="cta">Get Started Now</div>
  </div>

  <!-- FAQ -->
  <section class="abs" style="left:90px;top:2876px">
    <h2 class="sec-title" style="font-size:28px;line-height:28px">Frequently Asked<br><span class="hl">Questions</span></h2>
    <p class="small" style="font-size:8px;margin-top:14px;color:#4b5365">Got any specific question? Contact us now</p>
  </section>
  <div class="faq-item" style="top:2880px;height:72px;display:block;color:var(--blue)">
    <div style="display:flex;justify-content:space-between">Is Fiber Optic internet service faster than cable and DSL? <span>–</span></div>
    <p style="color:#636a7a;margin-top:22px;line-height:11px">Yes! Depending on your existing service, download and upload speeds from Marrowfen Fiber Optic can be 10 times faster or even more!</p>
  </div>
  <div class="faq-item" style="top:2956px">Can I keep my existing phone number? <span>+</span></div>
  <div class="faq-item" style="top:2996px">Can I use my existing telephones with Marrowfen VoIP phone service? <span>+</span></div>
  <div class="faq-item" style="top:3037px">What is the charge for installation? <span>+</span></div>
  <div class="faq-item" style="top:3077px">What if Marrowfen fiber isn't on my street? <span>+</span></div>
  <div class="faq-item" style="top:3117px">Can I use my existing telephones with Marrowfen VoIP phone service? <span>+</span></div>

  <!-- Subscribe -->
  <div class="abs subscribe">
    <h3>Subscribe &amp; receive news from <b>Brimvane</b></h3>
    <div class="sub-field"><span>Enter your email address...</span><span class="go">➤ Subscribe Now</span></div>
  </div>

  <!-- Footer -->
  <div class="fcol" style="left:85px"><h4>Company</h4>About<br>Careers</div>
  <div class="fcol" style="left:191px"><h4>Services</h4>Residential<br>Business<br>Services</div>
  <div class="fcol" style="left:295px"><h4>Packages</h4>Internet<br>Phone<br>VoIP</div>
  <div class="fcol" style="left:402px;line-height:12px"><h4>Working Hours</h4><b>Mon-Fri:</b><br>8am – 8pm<br><br><b>Sat:</b><br>12pm – 4pm<br><br><b>Sun:</b><br>4pm – 8pm</div>
  <div class="fcol" style="left:532px"><h4>Support</h4>Faqs<br>Contact</div>
  <div class="fcol" style="left:631px;line-height:12px"><h4>Contact</h4><b>Sales:</b><br>sales@marrowfen.com<br><br><b>Support:</b><br>support@marrowfen.com<br><br><b>Phone:</b><br>555-014-2200</div>
  <div class="abs" style="left:381px;top:3528px;width:32px;height:32px;border-radius:50%;background:var(--blue)"></div>
  <div class="abs" style="left:85px;top:3555px;font-size:6px;color:#7a8090">Privacy Policy &nbsp;&nbsp;&nbsp;&nbsp;&nbsp; Access Agreement</div>
  <div class="abs" style="left:684px;top:3552px;display:flex;gap:6px"><i style="width:10px;height:10px;border-radius:50%;background:var(--mist)"></i><i style="width:10px;height:10px;border-radius:50%;background:var(--mist)"></i></div>
  <div class="abs center" style="top:3570px;font-size:6px;color:#7a8090">© 2024 Brimvane - All Rights Reserved</div>
</main>
</body>
</html>
```